Brightmoor Card Company Business Cards

We are a trading card store with Zorblix, sports and other TCG cards, we need a business card design that encompasses a clean cut, modern style with a retro flare. website is brightmoorcardco.com for reference. Can utilize a comic book era feel or a more modern outdoor feel to utilize the "Pacific Northwest" elements of tress, mountains, etc.

Industry/Entity Type

Trading cards and collectibles

Contact Information for Business Card

business name, email address, phone number, name, owner job title

Font styles to use
Sans Serif

```html
<!DOCTYPE html>
<html lang="en">
<head>
<meta charset="utf-8">
<title>Brightmoor Card Company – Business Card</title>
<link rel="stylesheet" href="https://fonts.googleapis.com/css2?family=Montserrat:wght@400;500;600;700&display=swap">
<style>
  :root {
    --backdrop: #2f2f31;
    --card-white: #ffffff;
    --card-black: #232323;
    --accent-cyan: #15b6dc;
    --text-grey: #333333;
    --title-grey: #555555;
    --mountain-grey: #777777;
    --mountain-light: #8a8a8a;
    --badge-grey: #8a8a8a;
  }
  * { box-sizing: border-box; margin: 0; padding: 0; }
  html, body {
    width: 1200px; height: 1200px; overflow: hidden;
    background: var(--backdrop);
    font-family: "Montserrat", sans-serif;
  }
  .stage { position: relative; width: 1200px; height: 1200px; }
  .card {
    position: absolute; left: 220px;
    width: 760px; height: 434px;
    border-radius: 34px; overflow: hidden;
    box-shadow: 0 18px 40px rgba(0,0,0,.45);
  }
  .card--front { top: 150px; background: var(--card-white); }
  .card--back  { top: 620px; background: var(--card-black); }

  .contact {
    position: absolute; left: 60px; top: 112px;
    z-index: 2;
  }
  .contact__name {
    color: var(--accent-cyan); font-weight: 600;
    font-size: 44px; letter-spacing: 2px; line-height: 1;
  }
  .contact__title {
    color: var(--title-grey); font-weight: 400;
    font-size: 22px; letter-spacing: 2px; margin: 8px 0 18px;
  }
  .contact__list { list-style: none; }
  .contact__item {
    display: flex; align-items: center; gap: 12px;
    color: var(--text-grey); font-size: 21px; font-weight: 400;
    letter-spacing: .3px; margin-bottom: 10px; white-space: nowrap;
  }
  .contact__icon { width: 24px; height: 24px; flex: none; }

  .scenery {
    position: absolute; right: 0; bottom: 0;
    width: 270px; height: 330px;
    background: linear-gradient(170deg, var(--mountain-light), var(--mountain-grey));
    clip-path: polygon(0 62%, 22% 40%, 40% 22%, 62% 0, 100% 0, 100% 100%, 0 100%);
    z-index: 1;
  }

  .brand {
    position: absolute; inset: 0;
    display: flex; align-items: center; justify-content: center; gap: 16px;
  }
  .brand__dot {
    width: 30px; height: 30px; border-radius: 50%;
    background: var(--accent-cyan); flex: none;
  }
  .brand__name {
    color: var(--badge-grey); font-weight: 700;
    font-size: 32px; letter-spacing: 3px; text-transform: uppercase;
    white-space: nowrap;
  }
</style>
</head>
<body>
<main class="stage">
  <section class="card card--front">
    <div class="contact">
      <h1 class="contact__name">FULL NAME</h1>
      <p class="contact__title">TITLE</p>
      <ul class="contact__list">
        <li class="contact__item">
          <svg class="contact__icon" viewBox="0 0 24 24"><path fill="var(--accent-cyan)" d="M6.6 10.8a15 15 0 0 0 6.6 6.6l2.2-2.2c.3-.3.7-.4 1-.2 1.1.4 2.3.6 3.6.6.6 0 1 .4 1 1V20c0 .6-.4 1-1 1A17 17 0 0 1 3 4c0-.6.4-1 1-1h3.5c.6 0 1 .4 1 1 0 1.3.2 2.5.6 3.6.1.3 0 .7-.2 1z"/></svg>
          <span>(000) 000 0000</span>
        </li>
        <li class="contact__item">
          <svg class="contact__icon" viewBox="0 0 24 24"><g fill="none" stroke="var(--accent-cyan)" stroke-width="1.8"><circle cx="12" cy="12" r="10"/><ellipse cx="12" cy="12" rx="4.5" ry="10"/><path d="M2 12h20M4 7h16M4 17h16"/></g></svg>
          <span>www.brightmoorcardco.com</span>
        </li>
        <li class="contact__item">
          <svg class="contact__icon" viewBox="0 0 24 24"><path fill="var(--accent-cyan)" d="M2 5h20v14H2z"/><path fill="none" stroke="#fff" stroke-width="1.6" d="M2 5l10 8 10-8M2 19l7-7M22 19l-7-7"/></svg>
          <span>email@company.com</span>
        </li>
      </ul>
    </div>
    <div class="scenery" role="img" aria-label="Grey mountain range illustration"></div>
  </section>

  <section class="card card--back">
    <div class="brand">
      <span class="brand__dot"></span>
      <span class="brand__name">Brightmoor Card Company</span>
    </div>
  </section>
</main>
</body>
</html>
```